Label for Wines Design

I need a label design for a start-up business that makes grape wines. The label of wine features a picture frame on the edges of the wine bottle label. So each style of wine (red, white, sparkling, rose etc) will feature a different colour. As you can picture there is already a lot going on in this label.

My trademark is 'tamo', means 'Virgin pure love',type of wines: Sauvignon Blanc, Merlot, Pino noir etc. All in Caps, a Juxtaposition of old & modern. Bold & thick letters to grab attention on the wine store shelves. Maybe letter spacing squeezed together as the wine label is only 4inches wide...the text 'tamo' must fit on one line! No Cursive or curvy lines! Colors open to black, green, yellow, purple must be natural colors hues in nature.

New Zealand wines are New worlds wines,green and astringency,unique fruity, just as virgin pure love, is an infatuation, lovesickness, never forget......

Target Market(s)

New Zealand and Asian
food & wine lovers all ages

Industry/Entity Type

Business

Font styles to use
Decorative
Script

Colors

Designer to choose colors to be used in the design.

Requirements
Must have
• Front Label and back label
Nice to have
• Wines-feeling is green and astringency,unique fruity, just as virgin pure love, is an infatuation, lovesickness, never forget......

```html
<!DOCTYPE html>
<html lang="en">
<head>
<meta charset="utf-8">
<title>Tamo Wine Labels</title>
<link href="https://fonts.googleapis.com/css2?family=Oswald:wght@300;400&display=swap" rel="stylesheet">
<style>
  :root {
    --page: #ffffff;
    --white-panel: #f8f7e6;
    --white-frame-light: #d6e19c;
    --white-frame-mid: #c9d883;
    --white-frame-dark: #8c9a58;
    --white-ink: #333333;
    --white-accent: #7f8f45;
    --white-leaf-light: #d4e19a;
    --white-leaf-dark: #7f8f45;
    --red-panel: #050505;
    --red-frame-light: #e52128;
    --red-frame-mid: #c81d23;
    --red-frame-dark: #6e1215;
    --red-ink: #f4f4f4;
    --red-leaf-light: #ef2a2f;
    --red-leaf-dark: #6a1013;
  }
  * { margin: 0; padding: 0; box-sizing: border-box; }
  html, body { width: 1200px; height: 1000px; overflow: hidden; background: var(--page); }
  .canvas { position: relative; width: 1200px; height: 1000px; }
  .label { position: absolute; top: 247px; width: 222px; height: 503px; }
  .label--white { left: 88px; }
  .label--red { left: 338px; }
  .label__frame { position: absolute; inset: 0; }
  .label__name {
    position: absolute; top: 28px; left: 0; width: 100%;
    text-align: center; font-family: "Oswald", sans-serif; font-weight: 400;
    font-size: 96px; line-height: 1; letter-spacing: -2px;
  }
  .label__leaf {
    position: absolute; left: 28px; top: 130px; width: 182px; height: 255px;
    clip-path: polygon(18% 0, 30% 8%, 60% 40%, 100% 78%, 100% 86%, 55% 100%, 20% 95%, 0 40%);
  }
  .label__variety {
    position: absolute; top: 400px; left: 0; width: 100%; text-align: center;
    font-family: "Oswald", sans-serif; font-weight: 300; font-size: 20px;
  }
  .label__origin {
    position: absolute; top: 436px; left: 0; width: 100%; text-align: center;
    font-family: "Oswald", sans-serif; font-weight: 300; font-size: 16px;
  }
  .label__abv {
    position: absolute; top: 466px; left: 37px;
    font-family: "Oswald", sans-serif; font-weight: 300; font-size: 9px;
  }
  .label__volume {
    position: absolute; top: 460px; right: 38px;
    font-family: "Oswald", sans-serif; font-weight: 300; font-size: 15px;
  }
  .label--white .label__name { color: var(--white-ink); }
  .label--white .label__variety,
  .label--white .label__origin,
  .label--white .label__abv,
  .label--white .label__volume { color: var(--white-accent); }
  .label--white .label__leaf { background: linear-gradient(135deg, var(--white-leaf-dark), var(--white-leaf-light) 55%, var(--white-leaf-dark)); }
  .label--red .label__name,
  .label--red .label__origin,
  .label--red .label__abv,
  .label--red .label__volume,
  .label--red .label__variety { color: var(--red-ink); }
  .label--red .label__leaf { background: linear-gradient(135deg, var(--red-leaf-dark), var(--red-leaf-light) 55%, var(--red-leaf-dark)); }
</style>
</head>
<body>
<main class="canvas">

  <section class="label label--white">
    <svg class="label__frame" width="222" height="503" viewBox="0 0 222 503">
      <polygon points="0,0 222,0 208,14 14,14" fill="var(--white-frame-light)"/>
      <polygon points="222,0 222,503 208,489 208,14" fill="var(--white-frame-mid)"/>
      <polygon points="0,503 222,503 208,489 14,489" fill="var(--white-frame-dark)"/>
      <polygon points="0,0 14,14 14,489 0,503" fill="var(--white-frame-light)"/>
      <polygon points="0,240 14,233 14,489 0,503" fill="var(--white-frame-dark)"/>
      <rect x="14" y="14" width="194" height="475" fill="var(--white-panel)"/>
    </svg>
    <div class="label__name">TAMO</div>
    <div class="label__leaf" role="img" aria-label="Fern frond illustration in lime and olive greens"></div>
    <div class="label__variety">SAUVIGNON BLANC</div>
    <div class="label__origin">WINE OF NEW ZEALAND</div>
    <div class="label__abv">12% Vol</div>
    <div class="label__volume">750ml</div>
  </section>

  <section class="label label--red">
    <svg class="label__frame" width="222" height="503" viewBox="0 0 222 503">
      <polygon points="0,0 222,0 208,14 14,14" fill="var(--red-frame-mid)"/>
      <polygon points="222,0 222,503 208,489 208,14" fill="var(--red-frame-light)"/>
      <polygon points="0,503 222,503 208,489 14,489" fill="var(--red-frame-dark)"/>
      <polygon points="0,0 14,14 14,489 0,503" fill="var(--red-frame-mid)"/>
      <polygon points="0,240 14,233 14,489 0,503" fill="var(--red-frame-dark)"/>
      <rect x="14" y="14" width="194" height="475" fill="var(--red-panel)"/>
    </svg>
    <div class="label__name">TAMO</div>
    <div class="label__leaf" role="img" aria-label="Fern frond illustration in bright and deep reds"></div>
    <div class="label__variety">MERLOT</div>
    <div class="label__origin">WINE OF NEW ZEALAND</div>
    <div class="label__abv">12% Vol</div>
    <div class="label__volume">750ml</div>
  </section>

</main>
</body>
</html>
```